Australian Careers Business Needs 2 Banner Ad Design

We need a banner ad design for a new company based in Australia called Bright Sparrows. We provide career tools and insights to young professionals. Our target market is 20-30 year olds.

We would like to see designs that attract users on the site to click on the banner and sign up for a weekly newsletter. The newsletter will feature a blog, cheat sheets etc. Inspiration in their inbox!

The second banner is to attract users to sign up for a Horizon Gathering. They would click on it to find out more information and then register with their email address. This convention is a 1 day workshop designed to enhance young professionals abilities to give their best at work. There will CEO insights etc.

Use of images or flash is ok. Needs to look very professional and presented in accordance to the current colour scheme in place. Visit http://www.brightsparrows-demo.com/home to understand.

Banner sizes 300 x 250.
Mandatory use of Corporate Colours required on Font.
R66 G73 B74
R242 G240 B230
R38 G128 B138

No logo necessary.

Hi All,As both banners will feature on the Bright Sparrows site there is no need for a logo or hyperlink to the site.I would like to see some better images, and a bit more creative flair.Please don't use single female images as I am wanting to avoid the women in business perception. We cater to young professionals.Some suggestions for lines to utilise on the newsletter ad:Click here for weekly career tipsInvest in your career for free hereJoin the weekly conversationWeekly career tips in your inboxSign up for our weekly newsletterSome suggestions for lines to use on the horizon gathering ad:Register for the Horizon Gathering - Find out how to get ahead of your peersAre you a millennial climbing the corporate ladder? Find out how to rise to the topInterested in hearing from experts who recognise millennials are our future business leaders? Click here.Thanks,Megan Added Friday, April 3, 2015

Target Market(s)

20-30 years

Industry/Entity Type

Business

Font styles to use
Sans Serif

Requirements
Must have
• Please use images in the attached as options
Should not have
• NO LOGO - Its already onsite so not needed.

```html
<!DOCTYPE html>
<html lang="en">
<head>
<meta charset="utf-8">
<title>Bright Sparrows – Newsletter Banner Set</title>
<link rel="stylesheet" href="https://fonts.googleapis.com/css2?family=Arimo:wght@400;700&family=Montserrat:wght@500&display=swap">
<style>
  :root {
    --page-bg: #ffffff;
    --teal: #3a8a8c;
    --teal-deep: #2f7173;
    --brand-teal: #26808a;
    --ink: #42494a;
    --headline: #6b6f70;
    --orange: #f7993a;
    --orange-light: #fbc27f;
    --sky: #2fa6d3;
    --sky-light: #5cc3e8;
    --panel-top: #f4f7f8;
    --panel-mid: #d9ecf2;
    --red: #e52a30;
    --red-light: #f4585c;
    --red-dark: #6e0f12;
    --frame: #4a4f50;
  }
  * { box-sizing: border-box; margin: 0; padding: 0; }
  html, body { width: 1200px; height: 1200px; overflow: hidden; background: var(--page-bg); }
  .sheet {
    width: 850px; height: 850px; position: relative;
    transform: scale(1.41176); transform-origin: 0 0;
    font-family: "Arimo", Arial, sans-serif;
  }
  .banner {
    position: absolute; left: 290px; width: 300px; height: 250px;
    border: 1px solid var(--frame); overflow: hidden;
  }
  .banner--one { top: 26px; }
  .banner--two { top: 283px; }
  .banner--three { top: 541px; }
  .banner__art { position: absolute; inset: 0; width: 300px; height: 250px; display: block; }
  .brand {
    position: absolute; left: 60px; top: 10px; width: 180px;
    display: flex; align-items: center; gap: 8px; justify-content: center;
  }
  .brand__dot { width: 12px; height: 12px; border-radius: 50%; background: var(--brand-teal); flex: none; }
  .brand__name {
    font-family: "Montserrat", Arial, sans-serif; font-weight: 500;
    color: var(--brand-teal); font-size: 15px; letter-spacing: 1.5px; text-transform: uppercase;
  }
  .thumb {
    position: absolute; left: 33px; top: 83px; width: 42px; height: 41px;
    border: 1px solid #c9d3d6;
  }
  .thumb--suit { background: linear-gradient(135deg, #d7d9da, #2a2a2c 70%); }
  .thumb--phone { background: linear-gradient(160deg, #c9c9c9, #1d1f22 60%, #b7b9ba); }
  .thumb--typing { background: linear-gradient(140deg, #aebfd0, #e9d9ce 55%, #7f95ad); }
  .headline {
    position: absolute; left: 85px; top: 84px; width: 200px;
    color: var(--headline); font-weight: 700; line-height: 1.05;
  }
  .headline--large { font-size: 17.5px; }
  .headline--small { font-size: 14.5px; line-height: 1.25; top: 86px; }
  .email-field {
    position: absolute; left: 61px; top: 146px; width: 178px; height: 25px;
    background: #fff; border: 2px solid #5d6466; border-right-color: #cfd6d8; border-bottom-color: #cfd6d8;
    font-size: 11.5px; color: var(--ink); padding: 4px 0 0 10px;
  }
  .submit {
    position: absolute; left: 79px; top: 199px; width: 140px; height: 36px;
    border-radius: 3px; display: flex; align-items: center;
    background: linear-gradient(#f77b7e, var(--red-light) 45%, var(--red) 55%, #c81d22);
    box-shadow: 0 3px 4px rgba(0,0,0,.35);
  }
  .submit__label {
    width: 101px; text-align: center; color: #fff; font-weight: 700; font-size: 13px;
    text-shadow: 0 1px 1px rgba(0,0,0,.4); border-right: 1px solid rgba(0,0,0,.25);
    line-height: 36px;
  }
  .submit__icon { margin-left: 6px; width: 26px; height: 26px; display: block; }
  .caption {
    position: absolute; top: 797px; left: 0; width: 880px; text-align: center;
    font-size: 28px; color: #000;
  }
</style>
</head>
<body>
<div class="sheet">

  <svg width="0" height="0" style="position:absolute" aria-hidden="true">
    <defs>
      <linearGradient id="panelFill" x1="0" y1="0" x2="0" y2="1">
        <stop offset="0" stop-color="#ffffff"/>
        <stop offset="0.55" stop-color="#f2f7f9"/>
        <stop offset="1" stop-color="#d4e9f1"/>
      </linearGradient>
      <linearGradient id="skyFill" x1="0" y1="0" x2="0" y2="1">
        <stop offset="0" stop-color="#6fcdee"/>
        <stop offset="0.4" stop-color="#2fa6d3"/>
        <stop offset="1" stop-color="#1e8fc0"/>
      </linearGradient>
      <linearGradient id="swooshFill" x1="0" y1="0" x2="1" y2="0">
        <stop offset="0" stop-color="#f7993a"/>
        <stop offset="0.45" stop-color="#fcd3a0"/>
        <stop offset="1" stop-color="#f48a25"/>
      </linearGradient>
      <linearGradient id="capFill" x1="0" y1="0" x2="0" y2="1">
        <stop offset="0" stop-color="#ffffff"/>
        <stop offset="1" stop-color="#eceeef"/>
      </linearGradient>
      <g id="bannerArt">
        <rect width="300" height="250" fill="#3a8a8c"/>
        <rect y="160" width="300" height="90" fill="#2f7173"/>
        <rect x="26" y="30" width="249" height="160" rx="6" fill="url(#panelFill)"/>
        <path d="M26 130 H275 V184 a6 6 0 0 1 -6 6 H32 a6 6 0 0 1 -6 -6 Z" fill="url(#skyFill)" stroke="#9fdcf2" stroke-width="0.6"/>
        <path d="M0 62 Q170 62 300 8 V22 Q175 84 0 80 Z" fill="url(#swooshFill)"/>
        <path d="M0 0 H300 V8 Q170 62 0 62 Z" fill="url(#capFill)"/>
      </g>
      <g id="playIcon">
        <circle cx="13" cy="13" r="12" fill="#6e0f12" stroke="#f4a3a5" stroke-width="1.2"/>
        <path d="M10 7.5 L18 13 L10 18.5 Z" fill="#ffffff"/>
      </g>
    </defs>
  </svg>

  <section class="banner banner--one">
    <svg class="banner__art" viewBox="0 0 300 250" aria-hidden="true"><use href="#bannerArt"/></svg>
    <div class="brand"><span class="brand__dot"></span><span class="brand__name">Bright Sparrows</span></div>
    <div class="thumb thumb--suit" role="img" aria-label="Photo of a man in a suit adjusting his collar"></div>
    <h2 class="headline headline--large">5 ways to look more Professional</h2>
    <div class="email-field">Your email address</div>
    <div class="submit"><span class="submit__label">SUBMIT NOW</span><svg class="submit__icon" viewBox="0 0 26 26" aria-hidden="true"><use href="#playIcon"/></svg></div>
  </section>

  <section class="banner banner--two">
    <svg class="banner__art" viewBox="0 0 300 250" aria-hidden="true"><use href="#bannerArt"/></svg>
    <div class="brand"><span class="brand__dot"></span><span class="brand__name">Bright Sparrows</span></div>
    <div class="thumb thumb--phone" role="img" aria-label="Photo of a young professional checking a phone"></div>
    <h2 class="headline headline--small">What Interview Questions Should You KNow</h2>
    <div class="email-field">Your email address</div>
    <div class="submit"><span class="submit__label">SUBMIT NOW</span><svg class="submit__icon" viewBox="0 0 26 26" aria-hidden="true"><use href="#playIcon"/></svg></div>
  </section>

  <section class="banner banner--three">
    <svg class="banner__art" viewBox="0 0 300 250" aria-hidden="true"><use href="#bannerArt"/></svg>
    <div class="brand"><span class="brand__dot"></span><span class="brand__name">Bright Sparrows</span></div>
    <div class="thumb thumb--typing" role="img" aria-label="Photo of hands typing on a laptop keyboard"></div>
    <h2 class="headline headline--small">What Your Email Style Says About Your Personality</h2>
    <div class="email-field">Your email address</div>
    <div class="submit"><span class="submit__label">SUBMIT NOW</span><svg class="submit__icon" viewBox="0 0 26 26" aria-hidden="true"><use href="#playIcon"/></svg></div>
  </section>

  <p class="caption">Animated style</p>
</div>
</body>
</html>
```